Business card design for immigration consulting business

We need business card design for a company called T&R Migration Advisors Inc. This is a boutique immigration consulting and foreign recruitment agency owned and managed by two partners.
The business card will be used by partners \ owners of the business. The best way to describe the business would be committed to client, passionate about providing top-notch services, engaging, competent, professional

Target Market(s)

We work with individuals in and outside of Canada who need immigration advise as well as Canadian businesses looking to hire or sponsor foreign workers to Canada

Industry/Entity Type

Consulting

Contact Information for Business Card

The business card should have a standard size and horizontal lay-out

Font styles to use
Serif

Colors
f04a50
ec1f27
cbcbcb
dbdbdb

Requirements
Must have
• The business card mush have our logo, name of the company first and last name of the partner, position, phone, cell, fax, e-mail, skype, web-site
• Our first choice would a classic design with minimalist looks and elegant fonts and colors, but we are open minded to any creative ideas too
Nice to have
• On the other side it may have the description of the company: Immigration and Foreign Recruitment Services
• We're considering using stamping \ lettering on our business cards
• It would be nice if the business card would have white space, in case someone would like to make notes on it.
• One (back side) side of the business card can be all red with white logo
Should not have
• We do not want to have our pictures on the business card
• We do no want to have Canadian maple leaf on the business card as we already have one in our logo

```html
<!DOCTYPE html>
<html lang="en">
<head>
<meta charset="utf-8">
<title>T&amp;R Migration Advisors Inc. – Business Card</title>
<link href="https://fonts.googleapis.com/css2?family=Roboto:wght@400;500&family=Ubuntu:wght@400;500&display=swap" rel="stylesheet">
<style>
  :root {
    --page-bg: #e7e4e0;
    --card-red: #e3232b;
    --card-red-light: #f04a50;
    --card-white: #f6f4f0;
    --ink-gray: #4a4a4a;
    --brand-red: #ec1f27;
    --shadow: rgba(0,0,0,0.18);
  }
  html, body {
    margin: 0;
    padding: 0;
    width: 895px;
    height: 1200px;
    overflow: hidden;
    background: var(--page-bg);
  }
  .canvas {
    position: relative;
    width: 895px;
    height: 1200px;
  }
  .card {
    position: absolute;
    left: 97px;
    width: 700px;
    height: 400px;
    border-radius: 4px;
    box-shadow: 0 6px 18px var(--shadow);
    overflow: hidden;
  }
  .card--front {
    top: 110px;
    background: var(--card-red);
  }
  .front-pattern {
    position: absolute;
    inset: 0;
    background: var(--card-red);
  }
  .front-wordmark {
    position: absolute;
    inset: 0;
    display: flex;
    align-items: center;
    justify-content: center;
    font-family: "Ubuntu", sans-serif;
    font-weight: 500;
    font-size: 34px;
    color: var(--card-red-light);
    letter-spacing: 0.5px;
  }
  .card--back {
    top: 690px;
    background: var(--card-white);
  }
  .leaf-panel {
    position: absolute;
    left: 0;
    top: 48px;
    width: 300px;
    height: 352px;
    background: var(--brand-red);
    border-radius: 0 140px 0 0;
  }
  .holder {
    position: absolute;
    left: 60px;
    top: 210px;
    color: #fff;
    font-family: "Ubuntu", sans-serif;
    text-align: center;
    width: 230px;
  }
  .holder__name {
    font-size: 25px;
    font-weight: 500;
    margin: 0;
  }
  .holder__role {
    font-size: 15px;
    margin: 4px 0 0;
    opacity: 0.92;
  }
  .contacts {
    position: absolute;
    left: 392px;
    top: 118px;
    margin: 0;
    padding: 0;
    list-style: none;
    font-family: "Roboto", sans-serif;
    font-size: 17px;
    color: var(--ink-gray);
  }
  .contacts li {
    display: flex;
    align-items: center;
    height: 25px;
  }
  .contacts svg {
    width: 13px;
    height: 13px;
    margin-right: 10px;
    fill: var(--brand-red);
    flex: none;
  }
  .domain { color: var(--brand-red); }
</style>
</head>
<body>
<main class="canvas">

  <section class="card card--front" aria-label="Card front">
    <div class="front-pattern" role="img" aria-label="Red field with faint repeating leaf pattern"></div>
    <div class="front-wordmark">T&amp;R Migration Advisors Inc.</div>
  </section>

  <section class="card card--back" aria-label="Card back">
    <div class="leaf-panel" role="img" aria-label="Large red leaf emblem"></div>
    <div class="holder">
      <p class="holder__name">Evan Reid Marlow</p>
      <p class="holder__role">Partner / Owner</p>
    </div>
    <ul class="contacts">
      <li><svg viewBox="0 0 14 14"><circle cx="7" cy="7" r="7"/></svg>EvanMarlow</li>
      <li><svg viewBox="0 0 14 14"><path d="M1 4c0-2 2-3 6-3s6 1 6 3v1H10V3.5H4V5H1z M3 6h8l2 6H1z"/></svg>416-555-0142</li>
      <li><svg viewBox="0 0 14 14"><rect x="3" y="0" width="8" height="14" rx="1.5"/></svg>647-555-0188</li>
      <li><svg viewBox="0 0 14 14"><rect x="3" y="0" width="8" height="4"/><rect x="0" y="5" width="14" height="6" rx="1"/><rect x="3" y="9" width="8" height="5"/></svg>905-555-0117</li>
      <li><svg viewBox="0 0 14 14"><path d="M0 2h14v10H0z M1 3l6 5 6-5" stroke="#fff" stroke-width="1"/></svg>evan@tr-migration.com</li>
      <li><svg viewBox="0 0 14 14"><circle cx="7" cy="7" r="6.5"/><path d="M0.5 7h13M7 0.5v13M2.5 3.5h9M2.5 10.5h9" stroke="#fff" stroke-width="0.9" fill="none"/></svg>www.<span class="domain">tr-migration</span>.com</li>
    </ul>
  </section>

</main>
</body>
</html>
```